Cleaners Needs Bounce-Back Coupon For Laundry Service

We need a "bounce-back" coupon to attach to peoples dry cleaning orders that offers one free wash-n-fold laundry service. Right now we always attach their receipt to the bag that contains their dry cleaning when we return it. We'd like to also attach a coupon that will entice them to come try our laundry service.

Background on the service: We sort, wash, dry, and fold the laundry for customers and then neatly put it in a nice bag that makes returning very convenient. Their laundry comes out fresh, clean, smelling great, and without the hassle of doing it themselves. We have a great return rate. Most customers that try out the service become long term customers. The goal is to get our dry cleaning customers to come try it out.

Requirements:
* 5" x 8" and one-sided.
* To be printed on a standard color of card stock.
* Must incorporate our logo.
* Needs a place for us to fill in an expiration date. We'll fill in a date about two weeks out from the time they pick up their dry cleaning.
* Limit one coupon per customer.
* Limit 50 pounds of laundry per coupon.

Industry/Entity Type

Dry Cleaning

```html
<!DOCTYPE html>
<html lang="en">
<head>
<meta charset="utf-8">
<title>Fresh Fold Laundry – Bounce-Back Coupon</title>
<link rel="stylesheet" href="https://fonts.googleapis.com/css2?family=Arimo:ital,wght@0,700;1,700&display=swap">
<style>
  :root {
    --page-bg: #e4e5e8;
    --navy: #0a3aa8;
    --sky: #4fa3f2;
    --pale-sky: #8cc6fb;
    --field: #d6ebfb;
    --white: #ffffff;
    --label: #0f3aa0;
    --note: #e8821e;
    --bubble: #3fa6e6;
  }
  * { margin: 0; padding: 0; box-sizing: border-box; }
  html, body { width: 1200px; height: 835px; overflow: hidden; background: var(--page-bg); }
  body { position: relative; font-family: "Arimo", Arial, sans-serif; }

  .coupon {
    position: absolute;
    left: 130px; top: 124px;
    width: 940px; height: 588px;
  }
  .coupon-shape { position: absolute; inset: 0; width: 100%; height: 100%; }

  .brand {
    position: absolute;
    left: 70px; top: 140px;
    display: flex; align-items: center; gap: 16px;
  }
  .brand-mark { width: 46px; height: 46px; background: var(--navy); }
  .brand-name {
    font-weight: 700; font-size: 46px; color: var(--navy);
    letter-spacing: -0.5px;
  }

  .field {
    position: absolute;
    left: 66px; width: 696px; height: 57px;
    background: var(--field);
    border-radius: 15px;
    display: flex; align-items: center;
    padding-left: 18px;
    font-style: italic; font-weight: 700; font-size: 15.5px;
    color: var(--label);
  }
  .field-name { top: 271px; }
  .field-expiry { top: 346px; padding-left: 23px; }
  .field-blank { top: 421px; }

  .terms {
    position: absolute;
    top: 510px;
    font-style: italic; font-weight: 700; font-size: 15px;
    color: var(--note);
    white-space: nowrap;
  }
  .terms-customer { left: 74px; }
  .terms-weight { left: 366px; }

  .bubbles {
    position: absolute;
    left: 708px; top: 200px;
    width: 200px; height: 360px;
    border-radius: 30px;
    background: radial-gradient(ellipse at 55% 30%, rgba(63,166,230,0.35), rgba(63,166,230,0.08) 70%, rgba(255,255,255,0) 100%);
  }
</style>
</head>
<body>
  <section class="coupon">
    <svg class="coupon-shape" viewBox="0 0 940 588" aria-hidden="true">
      <rect x="0" y="0" width="940" height="588" rx="44" fill="var(--navy)"/>
      <path d="M0,72 C200,18 380,8 560,58 C710,100 830,104 940,72 L940,176 C830,176 720,160 560,110 C400,60 200,48 0,120 Z" fill="var(--sky)"/>
      <path d="M0,120 C200,48 400,60 560,110 C720,160 830,176 940,176 L940,200 C830,206 720,185 560,138 C400,92 210,82 0,152 Z" fill="var(--pale-sky)"/>
      <path d="M22,145 C220,84 400,94 560,138 C720,185 840,206 916,202 L916,526 Q916,566 876,566 L64,566 Q22,566 22,526 Z" fill="var(--white)"/>
    </svg>

    <div class="brand">
      <span class="brand-mark"></span>
      <span class="brand-name">Fresh Fold Laundry</span>
    </div>

    <div class="field field-name">NAME</div>
    <div class="field field-expiry">EXPIRATION DATE</div>
    <div class="field field-blank"></div>

    <p class="terms terms-customer">* Limit one coupon per customer</p>
    <p class="terms terms-weight">* Limit 50 pounds of laundry per coupon</p>

    <div class="bubbles" role="img" aria-label="Decorative soap bubbles and sparkles"></div>
  </section>
</body>
</html>
```